【ワイヤーフレーム】
http://kovexa.hostmir.example/client-check/lumera/waiya.png
※極力ワイヤーフレームにそって作成して下さい。

【画像について】
各メニューに配置する写真とメインイメージの写真をお纏め致しました。
必ずこの写真を配置して下さい★
https://19.filevault.example/0827-3c7e1a9f40b2d65e8814a0c9f7d31b62

【今のサイトの問題点】
・何のメニューか分かりづらい
・鍼、カリオンの強みが弱い
・サイトからのお問い合わせが全くない

【TOPデザイン作成にあたっての要望】
・予約アイコンをつける
・ファイシャルメニューが一番売りたいメニューとなります。
デザインは目立つように作成して下さい。
・針、カリオン併用治療を押したい
・高級街にあるので高級感があるデザイン
・ピクセルノート、スナップロウのアイコンを配置する

【ターゲット】
・新規顧客さま
会社員、主婦、お金もっている30代~40代

【サイトの目的】
・集客
・店舗の強みの打ち出し

【サイトマップ】
①TOP
②ABOUT US スタッフ
③トータルビューティー
④フェイシャルビュティー
⑤インナービュティー
⑥コラーゲンマシーン
⑦遺伝子検査・腸内フローラ
⑧料金表
⑨メニュー内容
⑩ニュース一覧
⑪ニュース詳細
⑫ブログ一覧
⑬ブログ詳細
⑭鍼・カリオンの説明
⑮よくある質問
⑯アクセス、治療時間、お問い合わせ
⑰求人(非表示 ページには設けなくていいです)
⑱物販 (非表示 ページには設けなくていいです)
⑲実績
⑳お客様の声

【カラー】
・茶色
・グレー

【参考サイト】
https://www.velkanis.example/ https://moravel-co.example
https://www.lumera1954.example/
茶系、グレー系
【ワイヤーフレーム】
※極力ワイヤーフレームにそって作成して下さい。

【画像について】
必ずこの写真を配置して下さい★
暗めの印象で作成をお願い致します。
濃い色味7:明るい色味3
今回4日間だけ延長させて頂きます。

この度はたくさんの応募有難うございます。

またの機会に是非宜しくお願い致します!

```html
<!DOCTYPE html>
<html lang="ja">
<head>
<meta charset="utf-8">
<title>銀座 ルメラ ライフ&amp;ビューティー</title>
<link href="https://fonts.googleapis.com/css2?family=Cormorant+Garamond:wght@500;600&family=Noto+Serif+JP:wght@400;500;600&family=Noto+Sans+JP:wght@400;500&display=swap" rel="stylesheet">
<style>
:root{
  --brown-deep:#2f1c12;
  --brown-dark:#3d2619;
  --brown:#6a4430;
  --brown-soft:#8a6a55;
  --beige:#f5f0ea;
  --beige-2:#ece3d9;
  --gray:#e4e2df;
  --text:#3b2a20;
  --muted:#7b6a5f;
  --white:#ffffff;
  --footer-text:#d9c7b8;
}
*{margin:0;padding:0;box-sizing:border-box}
html,body{width:1200px;height:2824px;overflow:hidden}
body{position:relative;background:var(--white);color:var(--text);font-family:"Noto Serif JP",serif}
.abs{position:absolute}

/* header */
.site-header{left:0;top:0;width:1200px;height:100px;background:var(--white);box-shadow:0 1px 0 var(--beige-2)}
.logo{left:60px;top:22px;display:flex;align-items:center;gap:10px;font-family:"Cormorant Garamond",serif;font-weight:600;font-size:40px;color:var(--brown-dark);letter-spacing:1px}
.logo-dot{width:10px;height:10px;border-radius:50%;background:var(--brown)}
.global-nav{right:50px;top:38px;display:flex;gap:40px;font-size:15px;color:var(--text)}
.global-nav .current{color:var(--brown-soft)}

/* menu area */
.menu-area{left:0;top:100px;width:1200px;height:660px;background:var(--beige)}
.menu-thumbs{left:240px;top:124px;display:flex;gap:15px}
.thumb{width:144px}
.thumb-img{width:144px;height:80px}
.thumb-label{margin-top:8px;font-size:12px;line-height:1.5;color:var(--text);text-align:center}

.card-box{background:var(--white);padding:30px 40px}
.card-en{font-family:"Cormorant Garamond",serif;font-size:14px;color:var(--muted)}
.card-title{font-size:24px;font-weight:500;margin-top:6px;color:var(--brown-dark)}
.card-text{font-size:13px;line-height:1.9;color:var(--muted);margin-top:14px}
.btn{display:inline-flex;align-items:center;justify-content:center;gap:10px;height:40px;padding:0 30px;background:var(--brown);color:var(--white);font-size:13px;border-radius:20px}

/* feature band */
.feature{left:0;top:760px;width:1200px;height:440px;background:var(--brown-dark)}
.feature-tag{left:160px;top:816px;padding:4px 14px;border:1px solid var(--brown-soft);color:var(--footer-text);font-size:13px}
.feature-title{left:160px;top:858px;font-size:32px;font-weight:500;color:var(--white)}
.feature-text{left:160px;top:922px;width:350px;font-size:13px;line-height:2;color:var(--footer-text)}
.feature-btn{left:160px;top:1100px;background:transparent;border:1px solid #b99a84;color:var(--white)}
.feature-photo{left:548px;top:828px;width:612px;height:344px}
.play{left:524px;top:970px;width:50px;height:50px;border-radius:50%;background:var(--white);display:flex;align-items:center;justify-content:center}

/* voices */
.voices{left:0;top:1200px;width:1200px;height:610px}
.voices-title{left:0;top:1330px;width:1200px;text-align:center;font-size:32px;font-weight:500;color:var(--brown-dark)}
.voices-rule{left:580px;top:1385px;width:40px;height:1px;background:var(--brown)}
.voices-lead{left:0;top:1405px;width:1200px;text-align:center;font-size:13px;line-height:1.9;color:var(--muted)}
.voice-card{top:1480px;width:360px;height:250px;background:var(--white);padding:28px 40px;text-align:center}
.voice-icon{width:60px;height:60px;border-radius:50%;background:var(--beige-2);margin:0 auto;display:flex;align-items:center;justify-content:center}
.voice-who{font-size:14px;margin-top:18px;color:var(--brown-dark)}
.voice-text{font-size:12.5px;line-height:1.9;color:var(--muted);margin-top:14px;text-align:left}

/* access */
.access{left:0;top:1810px;width:1200px;height:670px;background:var(--white)}
.access-info{left:60px;top:1840px;width:360px}
.access-name{font-size:17px;font-weight:600;color:var(--brown-dark)}
.access-block{font-size:12.5px;line-height:1.8;color:var(--text);margin-top:18px}
.access-block strong{font-weight:600;display:block}
.tel{left:100px;top:2368px;width:320px;height:64px;background:var(--brown);color:var(--white);font-family:"Cormorant Garamond",serif;font-size:32px;font-weight:600;display:flex;align-items:center;justify-content:center;letter-spacing:1px}
.map{left:440px;top:1810px;width:760px;height:670px}
.map-pin{left:808px;top:2130px;width:30px;height:30px;border-radius:50%;background:var(--brown-dark)}

/* footer */
.site-footer{left:0;top:2480px;width:1200px;height:344px;background:var(--brown-deep)}
.footer-logo{left:0;top:2500px;width:1200px;display:flex;justify-content:center;align-items:center;gap:10px;font-family:"Cormorant Garamond",serif;font-weight:600;font-size:36px;color:var(--white)}
.footer-logo .logo-dot{background:#b99a84}
.pagetop{right:60px;top:2515px;font-family:"Cormorant Garamond",serif;font-size:14px;letter-spacing:2px;color:var(--white)}
.footer-nav{font-size:13px;line-height:1.85;color:var(--footer-text);list-style:none}
.footer-nav li.sub{padding-left:12px}
.reserve{left:800px;top:2600px;width:220px;height:42px;border:1px solid #b99a84;border-radius:21px;color:var(--white);font-size:13px;display:flex;align-items:center;justify-content:center}
.social-label{left:800px;top:2668px;font-size:12px;color:var(--footer-text)}
.social{left:820px;top:2700px;display:flex;gap:26px}
.social span{width:36px;height:36px;border-radius:50%;background:#5a3e2e;display:block}
.footer-rule{left:60px;top:2780px;width:1080px;height:1px;background:#54392a}
.footer-bottom{top:2792px;font-size:11px;color:#a88f7d}
</style>
</head>
<body>

<header class="site-header abs">
  <div class="logo abs">Lumera<span class="logo-dot"></span></div>
  <nav class="global-nav abs">
    <span>当院について</span><span>カリオンと美容鍼灸</span><span class="current">メニュー</span><span>お知らせ</span><span>BLOG</span><span>Q&amp;A</span><span>アクセス</span>
  </nav>
</header>

<section class="menu-area abs"></section>
<div class="menu-thumbs abs">
  <div class="thumb"><div class="thumb-img" role="img" aria-label="フェイシャル施術の写真" style="background:linear-gradient(135deg,#d8b9a3,#9a6e55)"></div><p class="thumb-label">フェイシャルビューティーコース</p></div>
  <div class="thumb"><div class="thumb-img" role="img" aria-label="インナービューティー施術の写真" style="background:linear-gradient(135deg,#e6d3c4,#b38b70)"></div><p class="thumb-label">インナービューティーコース</p></div>
  <div class="thumb"><div class="thumb-img" role="img" aria-label="トータルビューティー施術の写真" style="background:linear-gradient(135deg,#c9a58c,#7d5540)"></div><p class="thumb-label">トータルビューティーコース</p></div>
  <div class="thumb"><div class="thumb-img" role="img" aria-label="コラーゲンマシンの写真" style="background:linear-gradient(135deg,#e9c9c6,#c0605a)"></div><p class="thumb-label">コラーゲンマシーン</p></div>
  <div class="thumb"><div class="thumb-img" role="img" aria-label="遺伝子検査の写真" style="background:linear-gradient(135deg,#e4eef2,#a9c1cc)"></div><p class="thumb-label">遺伝子・腸内フローラ</p></div>
</div>

<div class="abs" role="img" aria-label="コラーゲンマシンの施術室の写真" style="left:180px;top:280px;width:420px;height:110px;background:linear-gradient(120deg,#c9605a,#8c3a35)"></div>
<div class="card-box abs" style="left:240px;top:390px;width:360px;height:250px">
  <p class="card-en">Collagen Machine</p>
  <h3 class="card-title">コラーゲンマシン</h3>
  <p class="card-text">光の力で肌のハリを内側から整え、全身の美しさを引き出す施術です。</p>
  <div style="margin-top:18px"><span class="btn">さらに詳しく見る</span></div>
</div>

<div class="abs" role="img" aria-label="お腹に手を添えた女性の写真" style="left:600px;top:280px;width:420px;height:230px;background:linear-gradient(135deg,#efe3da,#c9a994)"></div>
<div class="card-box abs" style="left:600px;top:510px;width:380px;height:160px;padding:26px 40px">
  <p class="card-en">Gene・Intestinal Flora Inspection</p>
  <h3 class="card-title">遺伝子・腸内フローラ検査</h3>
  <p class="card-text" style="margin-top:8px">体質を知り、最適なケアをご提案します。</p>
</div>
<div class="abs" style="left:640px;top:668px"><span class="btn">さらに詳しく見る</span></div>

<section class="feature abs"></section>
<span class="feature-tag abs">当院のこだわり</span>
<h2 class="feature-title abs">鍼・カリオンとは</h2>
<p class="feature-text abs">鍼とカリオンを組み合わせた当院独自の施術で、肌の奥から健やかな美しさを育てます。体の巡りを整えながら、お一人おひとりに合わせたケアをご提供いたします。</p>
<span class="btn feature-btn abs">さらに詳しく見る</span>
<div class="feature-photo abs" role="img" aria-label="施術紹介の動画サムネイル" style="background:linear-gradient(110deg,#e2cbbd,#b9927b 60%,#8e6a57)"></div>
<div class="play abs"><svg width="16" height="18" viewBox="0 0 16 18"><path d="M2 1 L15 9 L2 17 Z" fill="#6a4430"/></svg></div>

<section class="voices abs" role="img" aria-label="柔らかくぼかした店内の写真" style="background:linear-gradient(180deg,#f7efe6,#ead9c8 50%,#f3e8dc)"></section>
<h2 class="voices-title abs">お客様の声</h2>
<div class="voices-rule abs"></div>
<p class="voices-lead abs">当院にお越しの皆様からいただいたご感想を、<br>お客様の声として一部ご紹介いたします。</p>
<div class="voice-card abs" style="left:240px">
  <div class="voice-icon"><svg width="24" height="28" viewBox="0 0 24 28"><path d="M12 1C6 1 2 5.5 2 11c0 7 10 16 10 16s10-9 10-16C22 5.5 18 1 12 1z" fill="#c9a994"/><circle cx="12" cy="11" r="4" fill="#fff"/></svg></div>
  <p class="voice-who">女性 千葉県 38歳 会社員</p>
  <p class="voice-text">施術を受けるたびに肌が明るくなり、周りから褒められることが増えました。丁寧な説明も安心できます。</p>
</div>
<div class="voice-card abs" style="left:602px">
  <div class="voice-icon"><svg width="24" height="28" viewBox="0 0 24 28"><path d="M12 1C6 1 2 5.5 2 11c0 7 10 16 10 16s10-9 10-16C22 5.5 18 1 12 1z" fill="#c9a994"/><circle cx="12" cy="11" r="4" fill="#fff"/></svg></div>
  <p class="voice-who">女性 東京都 42歳 主婦</p>
  <p class="voice-text">落ち着いた空間でゆっくり過ごせます。体の内側から整っていく実感があり、毎月通っています。</p>
</div>

<section class="access abs"></section>
<div class="access-info abs">
  <p class="access-name">銀座 ルメラ ライフ&amp;ビューティー</p>
  <p class="access-block">東京都中央区銀座七丁目4-12<br>ソレイユビル5F</p>
  <p class="access-block"><strong>電車でお越しの方</strong>銀座駅 A3出口より徒歩3分<br>東銀座駅 A1出口より徒歩5分</p>
  <p class="access-block"><strong>JR 山手線 有楽町駅</strong>中央口より徒歩8分</p>
  <p class="access-block">首都高速 京橋出口より約5分<br>近隣にコインパーキングあり</p>
  <p class="access-block"><strong>診療時間</strong>月〜金 11:00〜20:00<br>土・日・祝 10:00〜18:00</p>
</div>
<div class="tel abs">03-5820-4417</div>
<div class="map abs" role="img" aria-label="店舗周辺の地図" style="background:linear-gradient(135deg,#ecebe8,#dddbd7)"></div>
<div class="map-pin abs"></div>

<footer class="site-footer abs"></footer>
<div class="footer-logo abs">Lumera<span class="logo-dot"></span></div>
<span class="pagetop abs">PAGE TOP ▲</span>
<ul class="footer-nav abs" style="left:120px;top:2586px">
  <li>メニュー</li>
  <li class="sub">- フェイシャルビューティーコース</li>
  <li class="sub">- インナービューティーコース</li>
  <li class="sub">- トータルビューティーコース</li>
  <li class="sub">- コラーゲンマシーン</li>
  <li class="sub">- 遺伝子・腸内フローラ検査</li>
</ul>
<ul class="footer-nav abs" style="left:480px;top:2586px">
  <li>当院について</li>
  <li>カリオンと美容鍼灸</li>
  <li>メニュー</li>
  <li>お知らせ</li>
  <li>BLOG</li>
  <li>Q&amp;A</li>
  <li>アクセス</li>
</ul>
<div class="reserve abs">ご予約はこちら</div>
<span class="social-label abs">公式アカウント</span>
<div class="social abs"><span aria-label="ピクセルノート"></span><span aria-label="スナップロウ"></span><span aria-label="公式アカウント"></span></div>
<div class="footer-rule abs"></div>
<p class="footer-bottom abs" style="left:60px">個人情報の取り扱いについて ｜ 特定商取引法</p>
<p class="footer-bottom abs" style="right:60px">Copyright © 銀座 ルメラ ライフ&amp;ビューティー All Rights Reserved.</p>

</body>
</html>
```